Kx7Orbit WebSite

an educational website about tutoring, client will be surfing this site looking for a tutor, please see the attached images because the contains exactly what we need.
Updates

Project Deadline Extended Reason: something went wrong with the uploaded files, we are very sorry.thank you PlumeVault for the 5 days extension.now there is a 3 images describing the content of the three pages.good luck Added Friday, August 5, 2016

Target Market(s)

everyone

Industry/Entity Type

Education

Number of Pages Required

3 page

Font styles to use
Other font styles liked:
• something looks good in Arabic and english like "Droid Arabic Kufi"

Requirements
Must have
• the logo we attached, responsive design, simple, also try as much as you can Centering texts and layout because this website will have an Arabic version, Arabic is a Right-to-Left Language.
• a change language button,
Nice to have
• educational gestures.
• Centered texts and layout because this website will have an Arabic version, Arabic is a Right-to-Left Language.
• we have a web designer and we can download any template and add our logo and text to it, but.....
• we need creativity, so please stick to the contents in the images we attached, we need something very simple, more like a zorvia home page with little touch of filtering fields like the 5 dropdownlist and the gender selection buttons.
• try not to go far away from the contents we specified in the images, use less images or dont use images at all, try not to make the client scroll down,
Should not have
• too much colors or noisy layout or heavy media

```html
<!DOCTYPE html>
<html lang="en">
<head>
<meta charset="utf-8">
<title>Kx7Orbit – Home</title>
<link rel="stylesheet" href="https://fonts.googleapis.com/css2?family=Open+Sans:wght@400;600;700&family=Raleway:wght@400;500;600&family=Roboto+Slab:wght@400&display=swap">
<style>
:root{
  --brand:#1b75bc;
  --brand-light:#27a9e1;
  --brand-mid:#1a8fd0;
  --navy:#0f3d63;
  --orange:#f7941d;
  --ink:#222;
  --muted:#555;
  --footer:#333333;
  --footer-deep:#262626;
  --footer-line:#4a4a4a;
  --footer-text:#f0f0f0;
}
*{box-sizing:border-box;margin:0;padding:0}
html,body{width:956px;height:1200px;overflow:hidden;background:#fff}
body{position:relative;font-family:"Open Sans",Arial,sans-serif;color:var(--ink)}
.abs{position:absolute}
.top-rule{left:0;top:0;width:956px;height:2px;background:var(--brand-light)}

/* header */
.brand{left:74px;top:26px;display:flex;align-items:center;gap:8px;font-family:"Raleway",sans-serif;font-weight:600;font-size:36px;color:var(--brand)}
.brand-mark{width:30px;height:30px;background:var(--brand-light)}
.lang{left:797px;top:11px;width:83px;height:18px;border:1px solid #888;font-size:9px;display:flex;align-items:center;padding-left:4px;gap:9px;color:#333}
.lang .swatch{width:13px;height:9px;background:#c8102e;border-top:3px solid #fff;border-bottom:3px solid #1e3f8f}
.lang .caret{width:0;height:0;border-left:5px solid transparent;border-right:5px solid transparent;border-top:6px solid #333}
.nav{top:50px;display:flex;font-size:14.5px;color:#222}
.nav a{position:absolute;white-space:nowrap;color:inherit;text-decoration:none}
.nav .active{color:var(--brand-mid)}
.phone{left:754px;top:49px;display:flex;align-items:center;gap:6px;font-size:16px;color:#666}

/* hero */
.hero{left:0;top:94px;width:956px;height:450px}
.hero-photo{position:absolute;left:0;top:0;width:956px;height:420px;background:linear-gradient(100deg,#d6c7b9 0%,#e9e6e2 35%,#f2efea 55%,#d8c2ac 80%,#b9a79a 100%)}
.hero-arrow{position:absolute;top:188px;width:30px;height:28px;background:#3b3b3b;border:1px solid #777;display:flex;align-items:center;justify-content:center}
.hero-tag{position:absolute;left:418px;top:372px;width:240px;text-align:center;font-family:"Raleway",sans-serif;font-size:17px;line-height:17px;color:#fff}
.hero-name{position:absolute;left:100px;top:366px;font-family:"Raleway",sans-serif;font-weight:600;font-size:22px;color:#5cc3ee}

/* welcome */
.welcome-title{left:0;width:956px;top:564px;text-align:center;font-family:"Roboto Slab",serif;font-size:24px;color:var(--navy)}
.welcome-title span{color:var(--brand-mid)}
.welcome-rule{left:160px;top:602px;width:636px;border-top:1px dotted var(--brand-light)}
.welcome-text{left:106px;top:618px;width:744px;text-align:center;font-family:Arial,sans-serif;font-size:11.3px;line-height:17.6px;color:#333}
.welcome-text a{color:var(--brand);text-decoration:none}
.side-tab{left:924px;top:616px;width:32px;height:27px;background:var(--orange);color:#fff;font-size:22px;line-height:26px;text-align:center}

/* subjects */
.subject{top:708px;width:180px;text-align:center}
.subject-icon{width:84px;height:84px;margin:0 auto;border-radius:50%;background:var(--brand-light);box-shadow:0 3px 0 #1a4a6e;display:flex;align-items:center;justify-content:center}
.subject.maths .subject-icon{background:var(--orange)}
.subject h3{margin-top:14px;font-size:13.5px;font-weight:600;color:#222}
.subject.maths h3{color:var(--orange)}
.subject p{margin-top:11px;font-family:Arial,sans-serif;font-size:11.3px;line-height:17.6px;color:#333}
.subject a{display:inline-block;margin-top:9px;font-size:11.5px;font-weight:700;color:var(--brand)}
.subject.maths a{color:var(--orange)}

/* footer */
.footer{left:0;top:932px;width:956px;height:230px;background:var(--footer);color:var(--footer-text)}
.footer-bar{left:0;top:1162px;width:956px;height:38px;background:var(--footer-deep)}
.col-title{position:absolute;font-family:"Raleway",sans-serif;font-size:16.5px;color:#fff}
.col-rule{position:absolute;height:1px;background:#666}
.divider{position:absolute;top:30px;width:1px;height:150px;background:var(--footer-line)}
.links{position:absolute;left:78px;top:78px;list-style:none;font-size:11.3px;font-family:Arial,sans-serif}
.links li{height:31px;display:flex;gap:12px}
.links li::before{content:"›";color:#999}
.contact{position:absolute;left:250px;font-family:Arial,sans-serif;font-size:11.3px;line-height:16px;display:flex;gap:12px}
.contact svg{flex:none;margin-top:2px}
.field{position:absolute;left:466px;width:184px;height:23px;background:#fff;border-radius:2px;color:#333;font-family:Arial,sans-serif;font-size:10px;padding:6px 9px}
.submit{position:absolute;left:466px;top:184px;width:70px;height:25px;background:var(--brand-mid);color:#fff;font-family:Arial,sans-serif;font-weight:700;font-size:11px;display:flex;align-items:center;justify-content:center}
.footer-brand{position:absolute;left:730px;top:106px;display:flex;align-items:center;gap:7px;font-family:"Raleway",sans-serif;font-weight:600;font-size:28px;color:var(--brand-light)}
.footer-brand i{width:22px;height:22px;background:var(--orange)}
.copyright{left:75px;top:1174px;font-family:"Raleway",sans-serif;font-size:11px;color:#ddd}
.social{top:1168px;width:26px;height:26px;border-radius:50%;background:var(--brand-mid)}
</style>
</head>
<body>
<div class="abs top-rule"></div>

<header>
  <div class="abs brand"><span class="brand-mark"></span>Kx7Orbit</div>
  <div class="abs lang">ENGLISH <span class="swatch"></span><span class="caret"></span></div>
  <nav class="abs nav">
    <a class="active" style="left:390px">Home</a>
    <a style="left:462px">About Us</a>
    <a style="left:554px">Classes</a>
    <a style="left:626px">Contact Us</a>
  </nav>
  <div class="abs phone">
    <svg width="20" height="20" viewBox="0 0 20 20"><circle cx="10" cy="10" r="9" fill="none" stroke="#1a8fd0" stroke-width="1.4"/><path d="M7 5c-1 1-1 3 1 6s4 4 5 3l1-1-2-2-1 1c-1 0-3-2-3-3l1-1-2-3z" fill="#1a8fd0"/></svg>
    123-456-7890
  </div>
</header>

<section class="abs hero">
  <div class="hero-photo" role="img" aria-label="Photo of a tutor helping a young girl write at a classroom desk"></div>
  <svg class="abs" style="left:0;top:0" width="956" height="450" viewBox="0 0 956 450">
    <path d="M0 362 L956 402 L956 450 L0 450 Z" fill="#fff"/>
    <path d="M0 386 Q185 330 320 411 L255 438 L0 411 Z" fill="#27a9e1"/>
    <path d="M340 412 C420 340 700 290 808 370 C720 372 640 400 590 444 Z" fill="#1b75bc"/>
  </svg>
  <div class="hero-name">Kx7Orbit</div>
  <div class="hero-tag">Preparing Students For Successful Future</div>
  <div class="hero-arrow" style="left:6px"><svg width="10" height="12"><path d="M7 1 2 6l5 5" stroke="#fff" stroke-width="2.4" fill="none"/></svg></div>
  <div class="hero-arrow" style="left:916px"><svg width="10" height="12"><path d="M3 1l5 5-5 5" stroke="#fff" stroke-width="2.4" fill="none"/></svg></div>
</section>

<section>
  <h1 class="abs welcome-title" style="font-weight:400">Welcome to <span>Kx7Orbit</span></h1>
  <div class="abs welcome-rule"></div>
  <p class="abs welcome-text">Lorem ipsum dolor sit amet, consectetuer adipiscing elit, sed diam nonummy nibh euismod tincidunt ut laoreet dolore magna aliquam erat volutpat. Ut wisi enim ad minim veniam, quis nostrud exerci tation ullamcorper suscipit lobortis nisl ut aliquip ex ea commodo consequat. Duis autem vel eum iriure dolo....<a>Read&nbsp; More</a></p>
  <div class="abs side-tab">+</div>
</section>

<section>
  <div class="abs subject maths" style="left:75px">
    <div class="subject-icon"><svg width="40" height="40" viewBox="0 0 40 40" fill="#fff"><rect x="2" y="2" width="16" height="16"/><rect x="22" y="2" width="16" height="16"/><rect x="2" y="22" width="16" height="16"/><rect x="22" y="22" width="16" height="16"/><g stroke="#f7941d" stroke-width="2.4"><path d="M5 10h10M25 5l10 10M35 5 25 15M10 25v10M5 30h10M25 28h10M25 33h10"/></g></svg></div>
    <h3>Maths</h3>
    <p>Lorem ipsum dolor sit amet,<br>consectetuer adipi</p>
    <a>Read More</a>
  </div>
  <div class="abs subject" style="left:282px">
    <div class="subject-icon"><svg width="44" height="44" viewBox="0 0 44 44" fill="none" stroke="#fff" stroke-width="2.6"><path d="M24 8 34 18 20 28 14 40 4 30 16 24 Z"/><path d="M22 6 36 20"/><circle cx="38" cy="6" r="3"/><circle cx="16" cy="32" r="2" fill="#fff"/></svg></div>
    <h3>Science</h3>
    <p>Lorem ipsum dolor sit amet,<br>consectetuer adipi</p>
    <a>Read More</a>
  </div>
  <div class="abs subject" style="left:489px">
    <div class="subject-icon"><svg width="36" height="40" viewBox="0 0 36 40" fill="none" stroke="#fff" stroke-width="2.4"><rect x="3" y="2" width="30" height="34"/><text x="9" y="16" fill="#fff" stroke="none" font-family="Arial" font-weight="700" font-size="11">AB</text><path d="M8 24h20M8 30h20"/></svg></div>
    <h3>English</h3>
    <p>Lorem ipsum dolor sit amet,<br>consectetuer adipi</p>
    <a>Read More</a>
  </div>
  <div class="abs subject" style="left:697px">
    <div class="subject-icon"><svg width="36" height="44" viewBox="0 0 36 44" fill="none" stroke="#fff" stroke-width="2.4"><path d="M3 2h22l8 8v32H3z"/><circle cx="18" cy="14" r="6"/><path d="M9 26h18M9 31h18M9 36h18"/></svg></div>
    <h3>SAT/Test Prep</h3>
    <p>Lorem ipsum dolor sit amet,<br>consectetuer adipi</p>
    <a>Read More</a>
  </div>
</section>

<footer class="abs footer">
  <div class="divider" style="left:206px"></div>
  <div class="divider" style="left:426px"></div>
  <div class="divider" style="left:689px"></div>

  <h4 class="col-title" style="left:79px;top:32px;font-weight:400">Quick Links</h4>
  <div class="col-rule" style="left:74px;top:62px;width:98px"></div>
  <ul class="links"><li>Home</li><li>About Us</li><li>Classes</li><li>Contact Us</li></ul>

  <h4 class="col-title" style="left:247px;top:26px;font-weight:400">Contact Details</h4>
  <div class="col-rule" style="left:247px;top:62px;width:145px"></div>
  <div class="contact" style="top:78px"><svg width="12" height="16" viewBox="0 0 12 16"><path d="M6 0a6 6 0 0 1 6 6c0 4-6 10-6 10S0 10 0 6a6 6 0 0 1 6-6z" fill="#1a8fd0"/><circle cx="6" cy="6" r="2" fill="#333"/></svg><span>Street Name City Name<br>State Zipcode</span></div>
  <div class="contact" style="top:126px"><svg width="12" height="12" viewBox="0 0 12 12"><path d="M2 0C0 1 0 4 3 8s6 5 7 3l1-1-3-2-1 1C6 9 3 6 3 5l1-1-2-4z" fill="#1a8fd0"/></svg><span>123-456- 7890</span></div>
  <div class="contact" style="top:154px"><svg width="12" height="12" viewBox="0 0 12 12" fill="#1a8fd0"><rect x="3" y="0" width="6" height="4"/><rect x="0" y="4" width="12" height="6"/><rect x="3" y="8" width="6" height="4" fill="#fff"/></svg><span>123 - 456 -7890</span></div>
  <div class="contact" style="top:182px"><svg width="12" height="10" viewBox="0 0 12 10"><rect width="12" height="10" fill="#1a8fd0"/><path d="M0 0l6 5 6-5" stroke="#333" fill="none"/></svg><span>info@Kx7Orbit.com</span></div>

  <h4 class="col-title" style="left:466px;top:26px;font-weight:400">Quick Inquiry</h4>
  <div class="col-rule" style="left:466px;top:62px;width:189px"></div>
  <div class="field" style="top:80px">Name</div>
  <div class="field" style="top:110px">Email</div>
  <div class="field" style="top:139px;height:39px">Message</div>
  <div class="submit">SUBMIT</div>

  <div class="footer-brand"><i></i>Kx7Orbit</div>
</footer>

<div class="abs footer-bar"></div>
<p class="abs copyright">Copyright © 2016Kx7Orbit.All Rights Reserved</p>
<div class="abs social" style="left:789px" aria-label="Social link"></div>
<div class="abs social" style="left:822px" aria-label="Social link"></div>
<div class="abs social" style="left:857px" aria-label="Social link"></div>
</body>
</html>
```